Christmas in July Email Marketing Newsletter with landing page graphic needed

Email Marketing Campaign Newsletter for a Christmas in July Sale

Plan Your Christmas Shopping Now Smoky Mountains are the best place to get your Christmas Shopping completed at any of the over 100 brand named outlet stores!

This Sale will only last 72 Hours only! Call now to Save 19.68% off 11/25-12/25 Stay Days!

We need a version with the 72 hours Call to action and one with a only 24 hours left call to action. I have attached an example of the 72 hours call to action emblem.

The landing page image would just be the hero image here: http://bramblewoodstays.com/

Must have all properties logos like I have attached.
I attached a rough example of what I had come up with but know some one can make a more polished look

```html
<!DOCTYPE html>
<html lang="en">
<head>
<meta charset="utf-8">
<title>Christmas in July Sale</title>
<link rel="stylesheet" href="https://fonts.googleapis.com/css2?family=Montserrat:ital,wght@0,400;0,600;0,700;0,800;0,900;1,700;1,800;1,900&display=swap">
<style>
:root{
  --red:#e8443f;
  --deep-red:#c8141b;
  --ring-red:#b3120f;
  --orange:#ff7a00;
  --orange-dark:#e24400;
  --ink:#3d3d3d;
  --mint:#eef6ea;
  --navy:#1b3a78;
  --gold:#e2b23a;
  --white:#fff;
}
*{margin:0;padding:0;box-sizing:border-box}
html,body{width:857px;height:1200px;overflow:hidden;background:var(--white)}
.canvas{position:relative;width:857px;height:1200px;overflow:hidden;font-family:'Montserrat',sans-serif;
  background:linear-gradient(180deg,var(--mint) 0%,#f3f8f0 45%,var(--white) 70%)}
.decor-gifts{position:absolute;left:0;top:0;width:330px;height:290px;
  background:radial-gradient(ellipse at 30% 30%,#e04a45 0%,#f1a9a4 45%,rgba(238,246,234,0) 75%)}
.decor-pine{position:absolute;right:0;top:0;width:120px;height:90px;
  background:radial-gradient(ellipse at 80% 10%,#4f8a3c 0%,rgba(238,246,234,0) 70%)}
.headline{position:absolute;left:0;top:0;width:100%}
.headline span{position:absolute;font-style:italic;font-weight:900;color:var(--red);line-height:1;letter-spacing:-1px}
.headline .word-christmas{left:352px;top:90px;font-size:78px}
.headline .word-sale{left:598px;top:160px;font-size:80px}
.headline .word-july{left:470px;top:172px;font-size:24px;font-weight:700;color:var(--ink);letter-spacing:0}
.intro{position:absolute;left:37px;top:330px;width:660px;font-size:23px;line-height:44px;color:var(--ink);font-weight:400}
.intro strong{color:var(--red);font-weight:700}
.offer-band{position:absolute;left:0;top:563px;width:620px;height:177px;background:var(--deep-red)}
.offer-band .lead{position:absolute;left:45px;top:28px;color:var(--white);font-weight:700;font-size:21px}
.offer-band .save{position:absolute;left:37px;top:52px;color:var(--white);font-weight:900;font-size:64px;letter-spacing:-1px;white-space:nowrap}
.offer-band .pct{position:absolute;left:412px;top:60px;color:var(--white);font-weight:800;line-height:1;text-align:center}
.offer-band .pct b{display:block;font-size:34px}
.offer-band .pct i{display:block;font-style:normal;font-size:15px;font-weight:700}
.offer-band .dates{position:absolute;left:42px;top:131px;color:var(--white);font-weight:700;font-size:19px}
.countdown{position:absolute;left:499px;top:509px;width:284px;height:284px;border-radius:50%;
  background:radial-gradient(circle at 40% 35%,#ff8a1a 0%,var(--orange) 45%,var(--orange-dark) 100%);
  box-shadow:0 0 0 9px var(--ring-red),-6px 8px 18px 8px rgba(80,0,0,.35);color:var(--white);text-align:center}
.countdown .top{position:absolute;top:36px;left:0;width:100%;font-weight:700;font-size:15px;white-space:nowrap}
.countdown .hours{position:absolute;top:56px;left:0;width:100%;font-weight:900;font-style:italic;font-size:160px;line-height:1;
  text-shadow:3px 3px 0 #c41b10,6px 6px 10px rgba(0,0,0,.3)}
.countdown .bottom{position:absolute;top:205px;left:0;width:100%;padding-left:30px;font-weight:700;font-size:20px}
.properties{position:absolute;left:0;top:860px;width:100%;height:110px}
.property{position:absolute;top:0;height:100px;display:flex;align-items:center;justify-content:center;gap:8px;
  text-align:center;font-weight:700;font-size:20px;line-height:1.2;color:var(--navy)}
.property .mark{width:16px;height:16px;border-radius:50%;background:var(--navy);flex:none}
.p1{left:14px;width:230px}
.p2{left:262px;width:175px}
.p3{left:468px;width:176px}
.p4{left:660px;width:172px}
.wave{position:absolute;left:0;top:950px;width:857px;height:250px}
.brand-seal{position:absolute;left:540px;top:945px;width:240px;height:240px;border-radius:50%;background:var(--gold);
  display:flex;align-items:center;justify-content:center;text-align:center;padding:40px}
.brand-seal .name{font-weight:800;font-size:26px;line-height:1.2;color:var(--navy)}
</style>
</head>
<body>
<div class="canvas">
  <div class="decor-gifts" role="img" aria-label="Christmas gifts, stocking, candy cane, ornaments and pine branches"></div>
  <div class="decor-pine" role="img" aria-label="Pine branch"></div>

  <h1 class="headline">
    <span class="word-christmas">CHRISTMAS</span>
    <span class="word-july">IN JULY</span>
    <span class="word-sale">SALE</span>
  </h1>

  <p class="intro">Plan Your Christmas Shopping Now<br>
    <strong>Smoky Mountains</strong> are the best place to get your<br>
    Christmas Shopping completed at any of the over<br>
    <strong>100 brand named outlet stores!</strong></p>

  <div class="offer-band">
    <div class="lead">Call now to</div>
    <div class="save">SAVE 19.68</div>
    <div class="pct"><b>%</b><i>OFF</i></div>
    <div class="dates">11/25-12/25 Stay Days!</div>
  </div>

  <div class="countdown">
    <div class="top">This Sale will only Last</div>
    <div class="hours">72</div>
    <div class="bottom">Hours&nbsp;&nbsp;only!</div>
  </div>

  <div class="properties">
    <div class="property p1"><span class="mark"></span><span>Fernhollow<br>Waterpark Lodge</span></div>
    <div class="property p2"><span>Ridgeline<br>Retreat</span></div>
    <div class="property p3"><span>Maplecrest<br>Hotel</span></div>
    <div class="property p4"><span>Pinebrook<br>Inn</span></div>
  </div>

  <svg class="wave" viewBox="0 0 857 250" aria-hidden="true">
    <path d="M0 60 C200 20 420 120 857 40 L857 250 L0 250 Z" fill="#e9f2fb"/>
    <path d="M0 80 C220 40 430 150 857 70 L857 110 C440 190 220 90 0 130 Z" fill="#1a4fb0"/>
    <path d="M0 115 C230 80 450 185 857 105 L857 135 C450 215 230 115 0 150 Z" fill="#3b8be6"/>
    <path d="M0 150 C240 115 470 215 857 140 L857 160 C470 240 240 140 0 175 Z" fill="#8cc1f2"/>
  </svg>

  <div class="brand-seal">
    <span class="name">Bramblewood Stays</span>
  </div>
</div>
</body>
</html>
```